Business Card for Technology Startup

Design a 2-sided business card using the logo provided. We are a digital healthcare platform that provides a mobile app and web UI that helps caregivers, families, and doctors share information and provide better patient outcomes. We use AI and machine learning to help guide patients through their day-to-day life. The final design should communicate stability, peace, comfort, but also align with the image of an AI-driven technology startup.

I'd like the deliverable to by a Photoshop PSD file (with layers) that I can work with in pixlr.com. Should contain the following editable layers:
Name (ex. John Doe)
Title (ex. Founder / CEO)
Email (ex. info@brenvaxa.ai)
Phone (ex. (999) 333-5555)
Website (ex. https://brenvaxa.ai)

```html
<!DOCTYPE html>
<html lang="en">
<head>
<meta charset="utf-8">
<title>Brenvaxa Business Card – Two Sides</title>
<link rel="stylesheet" href="https://fonts.googleapis.com/css2?family=Poppins:wght@400;600;700&display=swap">
<style>
  :root {
    --board-blue: #035b96;
    --label-grey: #9a9a9a;
    --band-grey: #999999;
    --cyan-bright: #00fbff;
    --cyan-deep: #08b9ea;
    --ink: #0a0a0a;
    --paper: #ffffff;
  }
  * { margin: 0; padding: 0; box-sizing: border-box; }
  html, body {
    width: 1200px;
    height: 1200px;
    overflow: hidden;
  }
  body {
    position: relative;
    background: var(--board-blue);
    font-family: "Poppins", sans-serif;
    color: var(--ink);
  }

  .card {
    position: absolute;
    left: 307px;
    width: 586px;
    height: 360px;
    overflow: hidden;
  }
  .card--front {
    top: 204px;
    background: linear-gradient(45deg, var(--cyan-deep) 0%, var(--cyan-bright) 100%);
  }
  .card--back {
    top: 635px;
    background: var(--paper);
  }

  .brand {
    position: absolute;
    right: 62px;
    display: flex;
    align-items: center;
    gap: 12px;
  }
  .brand__dot {
    width: 16px;
    height: 16px;
    border-radius: 50%;
    background: var(--ink);
  }
  .card--back .brand__dot {
    background: linear-gradient(90deg, var(--cyan-deep), var(--cyan-bright));
  }
  .brand__name {
    font-weight: 700;
    font-size: 50px;
    line-height: 1;
    letter-spacing: 0.5px;
    color: var(--ink);
  }
  .card--front .brand { top: 236px; }
  .card--back .brand  { top: 238px; }

  .website {
    position: absolute;
    right: 62px;
    top: 296px;
    font-size: 18px;
    font-weight: 400;
    line-height: 1;
  }

  .contact {
    position: absolute;
    right: 62px;
    top: 70px;
    text-align: right;
    line-height: 1;
  }
  .contact__name {
    font-size: 21px;
    font-weight: 700;
  }
  .contact__title {
    margin-top: 8px;
    font-size: 14px;
    font-weight: 400;
  }
  .contact__email {
    margin-top: 18px;
    font-size: 14px;
  }
  .contact__phone {
    margin-top: 8px;
    font-size: 14px;
  }

  .side-label {
    position: absolute;
    left: 927px;
    display: flex;
    align-items: center;
    gap: 15px;
    color: var(--label-grey);
    font-family: "Poppins", sans-serif;
    font-size: 27px;
    font-weight: 400;
    line-height: 1;
  }
  .side-label svg { display: block; }
  .side-label--front { top: 370px; }
  .side-label--back  { top: 802px; }

  .footer-band {
    position: absolute;
    left: 0;
    bottom: 0;
    width: 1200px;
    height: 71px;
    background: var(--band-grey);
  }
  .footer-band__title {
    position: absolute;
    right: 66px;
    top: 17px;
    color: var(--paper);
    font-size: 27px;
    font-weight: 400;
    line-height: 1;
  }
</style>
</head>
<body>

  <section class="card card--front" aria-label="Card front">
    <div class="brand">
      <span class="brand__dot"></span>
      <span class="brand__name">brenvaxa</span>
    </div>
    <p class="website">www.brenvaxa.ai</p>
  </section>

  <div class="side-label side-label--front">
    <svg width="22" height="24" viewBox="0 0 22 24" aria-hidden="true"><polygon points="0,12 22,0 22,24" fill="#9a9a9a"/></svg>
    <span>SIDE 1</span>
  </div>

  <section class="card card--back" aria-label="Card back">
    <div class="contact">
      <p class="contact__name">John Doe</p>
      <p class="contact__title">Founder / CEO</p>
      <p class="contact__email">info@brenvaxa.ai</p>
      <p class="contact__phone">(999) 333-5555</p>
    </div>
    <div class="brand">
      <span class="brand__dot"></span>
      <span class="brand__name">brenvaxa</span>
    </div>
  </section>

  <div class="side-label side-label--back">
    <svg width="22" height="24" viewBox="0 0 22 24" aria-hidden="true"><polygon points="0,12 22,0 22,24" fill="#9a9a9a"/></svg>
    <span>SIDE 2</span>
  </div>

  <footer class="footer-band">
    <p class="footer-band__title">Design 3</p>
  </footer>

</body>
</html>
```